Zielgruppe
Wir sind einer von nur 2 Berufsverbänden für Ergotherapeut:innen
Für die zu erstellende Landingpage sind Zielgruppen: Patient:innen die Therapeutische Versorgung brauchen und deren Angehörige, sowie die Berufsgruppe der Heilmittelerbringer: Physiotherapeuten, Ergotherapeuten, Sprachtherapeuten, Logopäden, Podologen
Aufgabenstellung
GEFÜHL, welches mit der Landingpage verbunden werden muss: VERBINDLICH und WARM

```html
<!DOCTYPE html>
<html lang="de">
<head>
<meta charset="utf-8">
<title>Online-Wahllokal – Bundesverband Handlungstherapie e.V.</title>
<link href="https://fonts.googleapis.com/css2?family=Mulish:wght@400;600;700;800&family=Open+Sans:wght@400;700&display=swap" rel="stylesheet">
<style>
:root{
  --green:#3aa845;
  --green-deep:#16963f;
  --ballot-green:#1f9a3c;
  --text:#333;
  --grey-band:#f6f6f6;
  --yellow:#f2c100;
  --white:#fff;
}
*{box-sizing:border-box;margin:0;padding:0}
html,body{width:768px;height:1200px;overflow:hidden;background:var(--white)}
body{position:relative;font-family:"Mulish",sans-serif;color:var(--text)}
.abs{position:absolute}

.brand{left:306px;top:26px;display:flex;align-items:center;gap:10px}
.brand-dot{width:50px;height:50px;border-radius:50%;background:#9fd19a}
.brand-name{font-weight:700;font-size:10px;line-height:12px;color:#333;border-left:1px solid #333;padding-left:9px;padding-top:28px;height:62px}

.kicker{left:0;width:768px;top:126px;text-align:center;font-weight:700;font-size:17px;color:#333}
.headline{left:0;width:768px;top:150px;text-align:center;font-weight:800;font-size:30px;line-height:35px;color:var(--green)}

.band-grey{left:0;top:316px;width:768px;height:300px;background:var(--grey-band)}
.band-green{left:0;top:615px;width:768px;height:221px;background:var(--green-deep)}
.notch{left:502px;top:614px}

.portrait{left:150px;top:278px;width:212px;height:152px;border-radius:90px 90px 0 0;background:linear-gradient(180deg,#c9a98e 0%,#b58d72 35%,#6f9cc9 60%,#5a8cc0 100%)}
.pointer{left:316px;top:378px}

.ballot{left:106px;top:427px;width:272px;height:576px;background:var(--white);box-shadow:0 2px 6px rgba(0,0,0,.18);font-family:"Open Sans",sans-serif}
.ballot-year{position:absolute;top:6px;width:100%;text-align:center;font-family:"Mulish",sans-serif;font-size:8.5px;color:#333}
.ballot-title{position:absolute;top:25px;width:100%;text-align:center;font-family:"Mulish",sans-serif;font-weight:800;font-size:10.5px;color:var(--ballot-green)}
.ballot-intro{position:absolute;left:7px;right:6px;top:42px;font-size:6.2px;line-height:8px;color:#333;text-align:justify}
.ballot-intro b{font-weight:700}
.ballot-table{position:absolute;left:6px;top:77px;width:261px;border:1px solid var(--ballot-green)}
.row{display:flex;border-top:1px solid var(--ballot-green)}
.row:first-child{border-top:none}
.mark{width:32px;border-right:1px solid var(--ballot-green);display:flex;align-items:center;justify-content:center}
.topic{flex:1;position:relative;padding:4px 4px 3px 32px}
.topic h3{font-family:"Mulish",sans-serif;font-weight:800;font-size:8.5px;color:var(--ballot-green);margin-left:5px;margin-bottom:3px}
.topic ul{list-style:none;font-size:5.6px;line-height:8.4px;color:#333}
.topic li{padding-left:6px;position:relative}
.topic li::before{content:"✓";position:absolute;left:0;color:#555;font-size:5px}
.topic-icon{position:absolute;left:5px;top:50%;width:20px;height:20px;margin-top:-6px;border-radius:3px;background:#cfe8d2}
.ballot-foot{position:absolute;left:8px;top:555px;font-family:"Mulish",sans-serif;font-weight:800;font-size:7.4px;line-height:9.5px;color:#333}

.claim{left:392px;top:374px;font-weight:700;font-size:28.5px;line-height:27px;color:var(--green)}
.lead{left:392px;top:457px;width:272px;font-size:9px;line-height:14.5px;color:#333}
.lead-big{left:392px;top:512px;width:240px;font-size:11.6px;line-height:15px;color:#333}
.lead-big strong{color:var(--green);font-weight:700}

.field{height:29px;background:var(--white);font-size:11.5px;font-weight:600;color:#333;padding:8px 10px}
.f-name{left:392px;top:665px;width:131px}
.f-first{left:536px;top:665px;width:131px}
.f-mail{left:392px;top:706px;width:275px}
.cta{left:392px;top:746px;width:275px;height:51px;background:var(--yellow);display:flex;align-items:center;padding-left:18px;box-shadow:0 1px 3px rgba(0,0,0,.2)}
.cta-ja{font-weight:800;font-size:26px;color:#111;margin-left:8px;letter-spacing:-1px}
.cta-text{font-weight:700;font-size:11.5px;line-height:14.5px;color:#222;margin-left:6px}

.info{left:392px;width:262px;font-size:9px;line-height:14.5px;color:#333}
.info a{color:var(--green);text-decoration:underline}
.info-1{top:872px}
.info-2{top:930px;width:276px}

.share-label{left:0;width:768px;top:1042px;text-align:center;font-weight:700;font-size:11px;color:var(--green)}
.share{left:287px;top:1080px;display:flex;gap:14px}
.share-slot{width:22px;height:22px;border:1.6px solid #111;border-radius:50%}
.footer{left:0;width:768px;top:1155px;text-align:center;font-size:9px;color:#333}
</style>
</head>
<body>

<div class="abs brand">
  <div class="brand-dot"></div>
  <div class="brand-name">Bundesverband<br>Handlungstherapie e.V.</div>
</div>

<div class="abs kicker">Online-Wahllokal:</div>
<h1 class="abs headline">Wie die THERAPEUTISCHE<br>VERSORGUNG von Morgen aussieht,<br>bestimmst DU!</h1>

<div class="abs band-grey"></div>
<div class="abs band-green"></div>
<svg class="abs notch" width="58" height="24" viewBox="0 0 58 24"><polygon points="0,0 58,0 29,23" fill="#f6f6f6"/></svg>

<div class="abs portrait" role="img" aria-label="Foto: Mann im hellblauen Hemd hält den Stimmzettel"></div>
<svg class="abs pointer" width="60" height="34" viewBox="0 0 60 34" fill="none" stroke="#3aa845" stroke-width="2.4" stroke-linecap="round">
  <path d="M57 4 C36 1 17 10 6 29"/>
  <path d="M4 18 L6 30 L16 25"/>
</svg>

<div class="abs ballot">
  <div class="ballot-year">Bundestagswahl 2021</div>
  <div class="ballot-title">Stimmzettel zur Heilmittelversorgung</div>
  <p class="ballot-intro">Meine <b>Wahlentscheidung</b> hängt davon ab, wie entschlossen Sie für eine bessere <b>Heilmittelversorgung</b> von Morgen eintreten! Für die <b>Gesundheit</b> und <b>Arbeitsfähigkeit</b> der <b>Menschen</b> in <b>Deutschland</b> sind folgende Themen bei der Heilmittelversorgung besonders wichtig:</p>

  <div class="ballot-table">
    <div class="row" style="height:55px">
      <div class="mark"><svg width="26" height="26" viewBox="0 0 26 26"><circle cx="13" cy="13" r="12" fill="none" stroke="#1f9a3c" stroke-width="1.3"/><path d="M7 6 L19 20 M19 6 L7 20" stroke="#1f9a3c" stroke-width="3" stroke-linecap="round"/></svg></div>
      <div class="topic"><span class="topic-icon"></span><h3>Ausbildung</h3><ul><li>bundesweite Schulgeldfreiheit</li><li>Modernisierung der Berufsgesetze</li><li>Einführung einer Ausbildungsvergütung</li><li>Akademisierung mit Durchlässigkeit der Bildungswege</li></ul></div>
    </div>
    <div class="row" style="height:73px">
      <div class="mark"><svg width="26" height="26" viewBox="0 0 26 26"><circle cx="13" cy="13" r="12" fill="none" stroke="#1f9a3c" stroke-width="1.3"/><path d="M7 6 L19 20 M19 6 L7 20" stroke="#1f9a3c" stroke-width="3" stroke-linecap="round"/></svg></div>
      <div class="topic"><span class="topic-icon"></span><h3>Kompetenzen</h3><ul><li>Blankoverordnung ohne Wirtschaftlichkeitsprüfung innerhalb der Einführungsphase für alle Indikationen</li><li>Perspektive für den Direktzugang</li><li>Möglichkeit zur Verordnung von Hilfsmitteln und Digitalen Gesundheitsanwendungen</li><li>Inhaltliche und monetäre Förderung von interprofessionellen Teams</li></ul></div>
    </div>
    <div class="row" style="height:105px">
      <div class="mark"><svg width="26" height="26" viewBox="0 0 26 26"><circle cx="13" cy="13" r="12" fill="none" stroke="#1f9a3c" stroke-width="1.3"/><path d="M7 6 L19 20 M19 6 L7 20" stroke="#1f9a3c" stroke-width="3" stroke-linecap="round"/></svg></div>
      <div class="topic"><span class="topic-icon"></span><h3>Selbstverwaltung</h3><ul><li>Mitbestimmung im G-BA</li><li>Klare Regelungen bezüglich Transparenz und Informationsfreigabe über Vertrags- und Verhandlungsbeschlüsse unter Angabe der tragenden Gründe auch im Sinne einer Korruptionsprävention</li><li>Beteiligung an Networking der Gesundheitswirtschaft (finanziell) fördern</li><li>Förderung von Strukturen zur demokratischen Meinungsbildung</li><li>Maßgebliche Beteiligung an Digitalisierungsprozessen und -anwendungen</li></ul></div>
    </div>
    <div class="row" style="height:71px">
      <div class="mark"><svg width="26" height="26" viewBox="0 0 26 26"><circle cx="13" cy="13" r="12" fill="none" stroke="#1f9a3c" stroke-width="1.3"/><path d="M7 6 L19 20 M19 6 L7 20" stroke="#1f9a3c" stroke-width="3" stroke-linecap="round"/></svg></div>
      <div class="topic"><span class="topic-icon"></span><h3>Finanzierung</h3><ul><li>Durchgängige Ermöglichung wirtschaftlicher Preise</li><li>Bedarfsgerechte Heilmittelversorgung statt bloßer Mengensteuerung</li><li>Aufrechnungswillkür von Absetzungen nach § 51 SGB I und § 387 BGB durch die automatische Verrechnung von Leistungen mit der nächsten Abrechnung aufheben</li><li>Abschaffung von Zuzahlungen für Patient:innen</li></ul></div>
    </div>
    <div class="row" style="height:65px">
      <div class="mark"><svg width="26" height="26" viewBox="0 0 26 26"><circle cx="13" cy="13" r="12" fill="none" stroke="#1f9a3c" stroke-width="1.3"/><path d="M7 6 L19 20 M19 6 L7 20" stroke="#1f9a3c" stroke-width="3" stroke-linecap="round"/></svg></div>
      <div class="topic"><span class="topic-icon"></span><h3>Versorgung</h3><ul><li>Etablierung einer qualitätsbezogenen Versorgungsforschung</li><li>Statistik-Monitoring von Versorgungsquoten und heilmittelversorgungsrelevanten Daten</li><li>Klares Bekenntnis zu Heilmitteln als systemrelevanten Teil der flächendeckenden Versorgung</li></ul></div>
    </div>
    <div class="row" style="height:47px">
      <div class="mark"><svg width="26" height="26" viewBox="0 0 26 26"><circle cx="13" cy="13" r="12" fill="none" stroke="#1f9a3c" stroke-width="1.3"/><path d="M7 6 L19 20 M19 6 L7 20" stroke="#1f9a3c" stroke-width="3" stroke-linecap="round"/></svg></div>
      <div class="topic"><span class="topic-icon"></span><h3>Forschung</h3><ul><li>Heilmittelforschung etablieren und finanzieren</li><li>Perspektive auf Promotion für akademisch ausgebildete Ergotherapeut:innen</li></ul></div>
    </div>
    <div class="row" style="height:55px">
      <div class="mark"><svg width="26" height="26" viewBox="0 0 26 26"><circle cx="13" cy="13" r="12" fill="none" stroke="#1f9a3c" stroke-width="1.3"/><path d="M7 6 L19 20 M19 6 L7 20" stroke="#1f9a3c" stroke-width="3" stroke-linecap="round"/></svg></div>
      <div class="topic"><span class="topic-icon"></span><h3>Zukunft</h3><ul><li>Freie Berufsausübung ohne Umweg über das Heilpraktikerwesen ermöglichen</li><li>Ergotherapeuten bei allen Belangen der Versorgung mitdenken. (DMP etc.)</li></ul></div>
    </div>
  </div>
  <p class="ballot-foot">Berücksichtigen Sie diese Themen als Partei im Wahlkampf,<br>und meine Stimme ist Ihnen sicher!</p>
</div>

<h2 class="abs claim">Du hast es<br>in der Hand!</h2>
<p class="abs lead">Von Deiner Wahlentscheidung hängt es ab, wie entschlossen Politiker für eine bessere Therapeutische Versorgung von Morgen eintreten!</p>
<p class="abs lead-big">Versende den folgenden Wahlzettel an alle relevanten Politiker mit <strong>nur einem Klick</strong>!</p>

<div class="abs field f-name">Name</div>
<div class="abs field f-first">Vorname</div>
<div class="abs field f-mail">E-Mail-Adresse</div>
<div class="abs cta">
  <svg width="42" height="42" viewBox="0 0 42 42"><rect x="2" y="6" width="34" height="34" fill="none" stroke="#111" stroke-width="1.6"/><path d="M7 22 L17 38 L39 2" fill="none" stroke="#111" stroke-width="5" stroke-linejoin="round"/></svg>
  <span class="cta-ja">JA</span>
  <span class="cta-text">zur besseren<br>Therapeutischen Versorgung</span>
</div>

<p class="abs info info-1">Du willst wissen, wen wir konkret die Wahlzettel zukommen lassen? <a>Hier findest Du die Liste</a> — diese wird bei der Projektdurchführung 1:1 noch mitgeteilt.</p>
<p class="abs info info-2">Eine Forderung des Wahlzettels teilst Du nicht? <a>Hier kannst Du den Wahlzettel individualisieren</a> — darüber gibt es die Möglichkeit einzelne Positionen abzuwählen</p>

<div class="abs share-label">Share:</div>
<div class="abs share">
  <span class="share-slot"></span><span class="share-slot"></span><span class="share-slot"></span>
  <span class="share-slot"></span><span class="share-slot"></span><span class="share-slot"></span>
</div>

<div class="abs footer">© 2004-2021 Bundesverband Handlungstherapie e.V.</div>

</body>
</html>
```